Title: Iron Lantern Sub: A quiet road through winter - Book cover

I need a complete book cover, front, spine, and back.

Religions Book

This book is more about the Title so it should be strong and serious.

Like the color Deep Red and black, blue. Deep purple
Avoid greens, orange, yellows.

Maybe a picture of a strong hand on the Bible. OR someone yelling.

If any pictures are used they must be 100% royalty free with proof or a buyout of image.

I have attached a couple of designs that the client likes. Just as a reference. The exception they DIDN'T like the pictures in the book cover.

Please ask any questions to clarify.

Please see the file I just uploaded called 'Book Cover samples.png" The clients likes the Title: Salt and Ember" the best. Please create a design something closer to this. The like how the title jumps off the page with a 2D look.

Again the Title must standout, and any use of images must be a secondary to the design.

I am happy with we the designs that have been submitted so far.

I hope this helps you get closer.

Thank you

First of all I want to thank you for all of your designs. At the beginning the client thought he would like a picture that represented the title. But after looking at all of the designs. He has now decided NOT to have any pictures.

Here is what he wants

1. BOLD Font (San Serif only) no fancy versions for the Title "IRON LANTERN" in uppercase. The title font should have some dimension to it to appear 2D or 3D looks. Shiny look. It needs to looks like it jumping off the page.

2. The subtitle right below the title in San Serif font)

3. Background solid color either black, dark red, or dark blue. The background can be slightly textured or gradation fill, etc.

4. The cover must have a strong and bold statement.

Thank you again.

Please use this photo on the back cover.

Thank you

• A picture that over powers the Title.

```html
<!DOCTYPE html>
<html lang="en">
<head>
<meta charset="utf-8">
<title>Iron Lantern – Book Cover</title>
<link href="https://fonts.googleapis.com/css2?family=Montserrat:wght@400;500;600;700&display=swap" rel="stylesheet">
<style>
  :root {
    --black: #0b0b0c;
    --charcoal: #3a3a3c;
    --spine-dark: #151516;
    --spine-edge: #8a8a8c;
    --white: #ffffff;
    --gold-light: #f3e3b8;
    --gold-dark: #9c7a3e;
    --red: #e0161c;
    --red-deep: #a50d12;
    --sky-top: #4a5468;
    --sky-mid: #b9bccb;
    --ground: #3a2f5a;
    --ground-dark: #1a1530;
  }
  * { margin: 0; padding: 0; box-sizing: border-box; }
  html, body { width: 1200px; height: 843px; overflow: hidden; background: var(--white); }
  .cover {
    position: relative; width: 1200px; height: 843px; overflow: hidden;
    font-family: "Montserrat", "Helvetica Neue", Arial, sans-serif; color: var(--white);
  }

  /* Back cover */
  .back {
    position: absolute; left: 0; top: 0; width: 545px; height: 843px;
    background: linear-gradient(90deg, var(--black) 0%, #1c1c1e 55%, var(--charcoal) 100%);
  }
  .title-block {
    position: absolute; text-align: center;
    text-shadow: 0 1px 0 #d8d8d8, 0 2px 0 #b5b5b5, 0 4px 6px rgba(0,0,0,.6);
  }
  .title-main { display: block; font-weight: 700; line-height: 1; letter-spacing: 2px; }
  .title-rule {
    display: block; height: 5px; margin: 0 auto;
    background: linear-gradient(90deg, var(--gold-dark), var(--gold-light) 50%, var(--gold-dark));
  }
  .title-sub { display: block; font-weight: 700; line-height: 1; letter-spacing: 1px; }

  .back .title-block { left: 110px; top: 56px; width: 320px; }
  .back .title-main { font-size: 88px; }
  .back .title-rule { width: 292px; margin-top: 12px; }
  .back .title-sub { font-size: 52px; margin-top: 10px; }

  .blurb {
    position: absolute; left: 46px; top: 290px; width: 454px;
    font-size: 14px; font-variant: small-caps; line-height: 24.2px;
    text-align: justify; hyphens: auto;
  }
  .author-photo {
    float: left; width: 189px; height: 209px; margin: 3px 8px 6px 0;
    background: linear-gradient(180deg, #f4f4f4 0%, #d9c7b8 55%, #3c4a8a 100%);
  }
  .web-button {
    position: absolute; left: 48px; top: 737px; width: 444px; height: 44px;
    background: linear-gradient(180deg, var(--red) 0%, var(--red-deep) 100%);
    box-shadow: 0 2px 4px rgba(0,0,0,.6);
    font-size: 23px; font-weight: 600; letter-spacing: 1px; text-align: center; line-height: 44px;
  }

  /* Spine */
  .spine {
    position: absolute; left: 545px; top: 0; width: 113px; height: 843px;
    background: linear-gradient(90deg, var(--spine-edge) 0%, var(--charcoal) 4%, var(--spine-dark) 35%, var(--spine-dark) 65%, var(--charcoal) 96%, var(--spine-edge) 100%);
  }
  .spine-rule {
    position: absolute; top: 44px; width: 4px; height: 455px;
    background: linear-gradient(180deg, var(--gold-dark), var(--gold-light) 50%, var(--gold-dark));
  }
  .spine-rule.left { left: 20px; }
  .spine-rule.right { left: 89px; }
  .spine-title {
    position: absolute; left: 28px; top: 44px; width: 58px; height: 455px;
    writing-mode: vertical-rl; text-align: center; white-space: nowrap;
    font-size: 46px; font-weight: 600; line-height: 58px; letter-spacing: 1px;
  }
  .spine-author {
    position: absolute; left: 38px; top: 562px; width: 38px; height: 260px;
    writing-mode: vertical-rl; white-space: nowrap;
    font-size: 24px; font-weight: 600; font-variant: small-caps; line-height: 38px; letter-spacing: 1px;
  }

  /* Front cover */
  .front { position: absolute; left: 658px; top: 0; width: 542px; height: 843px; }
  .front-art {
    position: absolute; inset: 0;
    background:
      radial-gradient(ellipse 260px 380px at 55% 40%, rgba(255,255,255,.35), rgba(255,255,255,0) 70%),
      linear-gradient(180deg, var(--sky-top) 0%, var(--sky-mid) 48%, #8d86a6 60%, var(--ground) 72%, var(--ground-dark) 100%);
  }
  .title-panel {
    position: absolute; left: 75px; top: 0; width: 397px; height: 303px;
    background: linear-gradient(180deg, rgba(200,10,14,.94) 0%, rgba(224,22,28,.88) 100%);
  }
  .front .title-block { left: 75px; top: 62px; width: 397px; }
  .front .title-main { font-size: 100px; }
  .front .title-rule { width: 346px; margin-top: 14px; }
  .front .title-sub { font-size: 62px; margin-top: 10px; }
  .subtitle {
    position: absolute; left: 40px; top: 313px; width: 468px; text-align: center; white-space: nowrap;
    font-size: 26px; font-weight: 500; font-variant: small-caps; line-height: 44px;
    text-shadow: 0 2px 4px rgba(0,0,0,.45);
  }
  .front-author {
    position: absolute; left: 125px; top: 773px; width: 272px; height: 60px;
    background: rgba(20,14,36,.6);
    font-size: 26px; font-weight: 600; font-variant: small-caps; line-height: 60px; text-align: center; letter-spacing: 1px;
  }
</style>
</head>
<body>
<div class="cover">

  <section class="back">
    <h2 class="title-block">
      <span class="title-main">IRON</span>
      <span class="title-rule"></span>
      <span class="title-sub">LANTERN</span>
    </h2>
    <div class="blurb">
      <div class="author-photo" role="img" aria-label="Portrait photograph of the author"></div>
      Lorem ipsum dolor sit amet, consectetur adipiscing elit. In eget nibh eu nulla imperdiet feugiat. Cum sociis natoque penatibus et magnis dis parturient montes, nascetur ridiculus mus. Sed in ante consectetur sem feugiat eleifend ac vel enim. Fusce quis est in nisi pretium facilisis. Etiam adipiscing interdum libero, aliquam aliquet orci cursus quis. Aliquam lobortis lacus quis purus tempor pretium. Aliquam ut placerat dui. Integer dictum risus dui, sit amet consequat nunc blandit ac. Aenean porttitor eros at felis ornare feugiat. Aenean sit amet nulla sem. Proin sem neque, imperdiet aliquet pulvinar et, hendrerit nec augue. Interdum et malesuada fames ac ante ipsum primis in faucibus.
    </div>
    <div class="web-button">WWW.MARTINHALE.COM</div>
  </section>

  <section class="spine">
    <span class="spine-rule left"></span>
    <span class="spine-rule right"></span>
    <div class="spine-title">IRON LANTERN</div>
    <div class="spine-author">Martin Hale</div>
  </section>

  <section class="front">
    <div class="front-art" role="img" aria-label="Photograph of a woman with raised arms beside an empty wheelchair in an open meadow under rays of light"></div>
    <div class="title-panel"></div>
    <h1 class="title-block">
      <span class="title-main">IRON</span>
      <span class="title-rule"></span>
      <span class="title-sub">LANTERN</span>
    </h1>
    <p class="subtitle">A Quiet Road Through Winter</p>
    <div class="front-author">Martin Hale</div>
  </section>

</div>
</body>
</html>
```